3月15日にガールズバーをオープン致しました。
ビルの入り口に置いて使うA1立て看板の製作をお願いします。
A4など縮小サイズでもいただけると助かります。
白を基調とした夜でも目立つ感じにしたいです。

セット料金 40分2000円 tax&service 20%

チャージのみ1時間1500円 tax&service 15

クレジットチャージ 10%
飲み放題付き (焼酎 ウイスキー カクテルなど)
ビル3階 席数17席  団体客歓迎

若いギャル系の女の子の写真を大きく入れて頂きたいのですが素材が無く
困ってます。素材をお持ちかたにお願いしたいと思ってます。

現在の看板を添付致しました。ご参考までに。
文章は記載しないでも大丈夫です。

店舗名 Sunflower(サンフラワー)です。

よろしくお願いします。
資料を再添付致しました。よろしくお願いします。
依頼金額を25000円に変更して、延長しました。
提案下さった皆様ありがとうございます。
もう少し提案を見させていただけたらと思います。

具体的なイメージをデザベース様の過去の事例で近いものを添付致しました。
よろしくお願いします。

最初に思い描いてたイメージより良かったです
女の子と背景のピンクもかわいいくて満足です。

ありがとうございました!

提案くださった皆様ありがとうございます!
修正をしてくださった皆様も早急な対応に感謝致します。

ありがとうございました!

```html
<!DOCTYPE html>
<html lang="ja">
<head>
<meta charset="utf-8">
<title>Sunflower Girl's Bar Sign</title>
<link href="https://fonts.googleapis.com/css2?family=M+PLUS+Rounded+1c:wght@500;800&family=Playfair+Display:wght@700&display=swap" rel="stylesheet">
<style>
:root{
  --pink:#e8388a;
  --pink-deep:#c21d6d;
  --pink-soft:#f7c6dd;
  --pink-pale:#fdeef5;
  --white:#ffffff;
  --ink:#3a2230;
  --gold:#f3c64a;
}
*{margin:0;padding:0;box-sizing:border-box}
html,body{width:896px;height:1200px;overflow:hidden;background:#f2f2f2}
.sign{position:relative;width:896px;height:1200px;overflow:hidden;
  background:linear-gradient(180deg,var(--white) 0%,var(--pink-pale) 60%,var(--pink-soft) 100%);
  font-family:"M PLUS Rounded 1c",sans-serif;color:var(--ink)}
.model-photo{position:absolute;left:320px;top:310px;width:576px;height:740px;
  background:radial-gradient(ellipse at 55% 35%,#f6d9b8 0%,#e9b48a 22%,#d99a4a 38%,#b0528c 62%,#7c2f6e 100%)}
.tagline{position:absolute;top:40px;left:0;width:100%;text-align:center;line-height:1;
  font-weight:800;font-size:30px;color:var(--pink);letter-spacing:4px}
.kind{position:absolute;top:92px;left:70px;font-family:"Playfair Display",serif;line-height:1;
  font-size:52px;color:var(--ink);letter-spacing:2px}
.shop-name{position:absolute;top:152px;left:140px;font-weight:800;font-size:112px;line-height:1;
  color:var(--pink);letter-spacing:2px;white-space:nowrap}
.shop-kana{position:absolute;top:274px;left:420px;font-weight:500;font-size:24px;line-height:1;color:var(--pink-deep)}
.prices{position:absolute;left:40px;top:340px;display:flex;flex-direction:column;gap:50px}
.price{position:relative;display:flex;align-items:center}
.price-heart{width:92px;height:84px;flex:none}
.price-label{position:absolute;left:0;width:92px;top:22px;text-align:center;color:var(--white);
  font-weight:800;font-size:17px;line-height:1.15}
.price-amount{margin-left:10px;font-weight:800;font-size:72px;color:var(--ink);line-height:1;white-space:nowrap;
  text-shadow:0 0 6px var(--white),0 0 2px var(--white)}
.price-amount small{font-size:34px}
.price-note{position:absolute;left:104px;top:86px;font-size:18px;line-height:1;color:var(--pink-deep);font-weight:500;white-space:nowrap}
.drink-badge{position:absolute;left:40px;top:660px;width:264px;padding:18px 12px;border-radius:18px;
  background:var(--pink);color:var(--white);text-align:center;font-weight:800;font-size:30px;line-height:1.3}
.drink-badge span{display:block;font-size:15px;font-weight:500;white-space:nowrap}
.footer{position:absolute;left:0;bottom:0;width:100%;height:150px;background:var(--pink);
  display:flex;align-items:center;justify-content:space-between;padding:0 40px;color:var(--white)}
.footer-info{font-weight:800;font-size:40px;line-height:1.25}
.footer-info small{display:block;font-size:20px;font-weight:500}
.burst{position:absolute;right:50px;bottom:170px;width:190px;height:190px}
.burst-text{position:absolute;right:50px;bottom:170px;width:190px;height:190px;display:flex;flex-direction:column;
  align-items:center;justify-content:center;font-weight:800;font-size:34px;color:var(--pink-deep);line-height:1.1}
.burst-text small{font-size:18px}
</style>
</head>
<body>
<div class="sign">
  <div class="model-photo" role="img" aria-label="Large photo of a young woman with styled blonde hair in a pink and purple outfit"></div>

  <p class="tagline">気軽に寄れるガールズバー</p>
  <p class="kind">GIRL'S BAR</p>
  <h1 class="shop-name">Sunflower</h1>
  <p class="shop-kana">サンフラワー</p>

  <div class="prices">
    <div class="price">
      <svg class="price-heart" viewBox="0 0 92 84"><path d="M46 82 C10 56 0 40 0 24 C0 10 11 0 24 0 C34 0 42 6 46 14 C50 6 58 0 68 0 C81 0 92 10 92 24 C92 40 82 56 46 82Z" fill="var(--pink)"/></svg>
      <span class="price-label">セット<br>料金</span>
      <span class="price-amount">40<small>分</small> 2,000<small>円</small></span>
      <span class="price-note">tax&amp;service 20%</span>
    </div>
    <div class="price">
      <svg class="price-heart" viewBox="0 0 92 84"><path d="M46 82 C10 56 0 40 0 24 C0 10 11 0 24 0 C34 0 42 6 46 14 C50 6 58 0 68 0 C81 0 92 10 92 24 C92 40 82 56 46 82Z" fill="var(--pink)"/></svg>
      <span class="price-label">チャージ<br>のみ</span>
      <span class="price-amount">60<small>分</small> 1,500<small>円</small></span>
      <span class="price-note">tax&amp;service 15%</span>
    </div>
  </div>

  <div class="drink-badge">飲み放題付き<span>焼酎・ウイスキー・カクテルなど</span></div>

  <svg class="burst" viewBox="0 0 190 190"><polygon fill="var(--gold)" points="95,0 112,35 150,18 145,58 185,65 155,92 185,120 145,128 150,170 112,152 95,190 78,152 40,170 45,128 5,120 35,92 5,65 45,58 40,18 78,35"/></svg>
  <div class="burst-text"><small>団体客</small>歓迎!</div>

  <div class="footer">
    <p class="footer-info">ビル3階 席数17席<small>クレジットチャージ 10%</small></p>
    <p class="footer-info">3/15 OPEN</p>
  </div>
</div>
</body>
</html>
```